Zephyrkin Climate Services WA Truck

I want a truck desing that screams Professional, Friendly and serious about work. you can find some of our work on our website, facebook and instagram.
https://zephyrkinclimate.com.au/
https://www.instagram.com/zpkhvac/
https://www.facebook.com/profile.php?id=73829106548213

The design needs to include our refrigeration license: AU47325 and electrical License: EC58913
I want the colours to be consistent with my Logo.

Key Notes to be included in the design, I want to let people know we do the following;
- Commercial and Residential
- Repairs, Service and Installation
- Reverse cycle ducted Air Conditioning
- Wall Split Air Conditioning
- Ceiling Cassettes
- Evaporative Air Conditioning
- Cool Rooms
- Display Fridges
- Beer Chillers

```html
<!DOCTYPE html>
<html lang="en">
<head>
<meta charset="utf-8">
<title>Zephyrkin Climate Services WA – Truck Box Wrap</title>
<link rel="stylesheet" href="https://fonts.googleapis.com/css2?family=Oswald:wght@500&family=Saira:wght@600;700&display=swap">
<style>
  :root {
    --canvas-bg: #eef1f4;
    --wrap-white: #ffffff;
    --brand-orange: #f0701e;
    --brand-orange-light: #f79a2c;
    --brand-blue: #1c63b0;
    --brand-navy: #1b4f8c;
    --text-white: #ffffff;
  }
  html, body {
    margin: 0;
    padding: 0;
    width: 1200px;
    height: 1200px;
    overflow: hidden;
    background: var(--canvas-bg);
  }
  .canvas {
    position: relative;
    width: 1200px;
    height: 1200px;
    display: flex;
    align-items: center;
    justify-content: center;
  }
  .box-wrap {
    width: 1120px;
    height: 540px;
    display: block;
    box-shadow: 0 6px 24px rgba(0,0,0,0.12);
  }
  .service-list text {
    font-family: "Oswald", sans-serif;
    font-weight: 500;
    font-size: 21px;
    fill: var(--text-white);
    letter-spacing: 0.3px;
  }
  .bullet { fill: var(--brand-blue); }
  .licence {
    font-family: "Oswald", sans-serif;
    font-weight: 500;
    font-size: 22px;
    fill: var(--text-white);
  }
  .brand-name {
    font-family: "Saira", sans-serif;
    font-weight: 700;
    fill: var(--brand-orange);
  }
  .phone {
    font-family: "Saira", sans-serif;
    font-weight: 700;
    font-size: 52px;
    fill: var(--text-white);
  }
  .website {
    font-family: "Saira", sans-serif;
    font-weight: 700;
    font-size: 21px;
    fill: var(--brand-navy);
  }
</style>
</head>
<body>
<main class="canvas">
  <svg class="box-wrap" viewBox="0 0 1120 540" xmlns="http://www.w3.org/2000/svg" aria-label="Zephyrkin Climate Services WA truck side panel">
    <defs>
      <linearGradient id="orangeFill" x1="0" y1="0" x2="1" y2="1">
        <stop offset="0" stop-color="var(--brand-orange)"/>
        <stop offset="1" stop-color="var(--brand-orange-light)"/>
      </linearGradient>
    </defs>

    <rect class="panel-base" width="1120" height="540" fill="var(--wrap-white)"/>

    <path class="orange-field" fill="url(#orangeFill)"
      d="M0 0 H345 C325 130 380 250 520 305 C610 340 700 345 780 365 C900 395 1030 430 1120 458 V540 H0 Z"/>

    <path class="blue-swoosh" fill="none" stroke="var(--brand-blue)" stroke-width="12"
      d="M368 0 C350 125 400 240 540 296 C600 320 650 330 690 336"/>
    <path class="blue-line" fill="none" stroke="var(--brand-blue)" stroke-width="7"
      d="M850 392 C940 412 1040 440 1120 462"/>

    <path class="blue-corner" fill="var(--brand-navy)" d="M0 360 C90 410 200 470 300 540 H0 Z"/>

    <g class="service-list">
      <circle class="bullet" cx="30" cy="38" r="4"/><text x="40" y="45">WALL SPLIT AIR CONDITIONING</text>
      <circle class="bullet" cx="30" cy="70" r="4"/><text x="40" y="77">CEILING CASSETTES</text>
      <circle class="bullet" cx="30" cy="102" r="4"/><text x="40" y="109">EVAPORATIVE AIR CONDITIONING</text>
      <circle class="bullet" cx="30" cy="134" r="4"/><text x="40" y="141">COOL ROOMS</text>
      <circle class="bullet" cx="30" cy="166" r="4"/><text x="40" y="173">DISPLAY FRIDGES</text>
      <circle class="bullet" cx="30" cy="198" r="4"/><text x="40" y="205">BEER CHILLERS</text>
      <circle class="bullet" cx="30" cy="230" r="4"/><text x="40" y="237">COMMERCIAL AND RESIDENTIAL</text>
      <circle class="bullet" cx="30" cy="262" r="4"/><text x="40" y="269">REPAIRS, SERVICE AND INSTALLATION</text>
      <circle class="bullet" cx="30" cy="294" r="4"/><text x="40" y="301">REVERSE CYCLE DUCTED AIR</text>
      <text x="40" y="331">CONDITIONING</text>
    </g>

    <text class="licence" x="26" y="465">AU47325</text>
    <text class="licence" x="26" y="495">LIC# EC58913</text>

    <circle class="brand-dot" cx="812" cy="150" r="34" fill="var(--brand-blue)"/>
    <text class="brand-name" x="812" y="245" text-anchor="middle" font-size="52">ZEPHYRKIN</text>
    <text class="brand-name" x="812" y="282" text-anchor="middle" font-size="22" letter-spacing="3">CLIMATE SERVICES WA</text>

    <text class="phone" x="620" y="463" text-anchor="middle">(870) 482-3316</text>
    <text class="website" x="620" y="500" text-anchor="middle">www.zephyrkinclimate.com.au</text>
  </svg>
</main>
</body>
</html>
```